Business Card Design Project

Looking to have a new business card created.

The card needs to be sort of two cards attached in the centre creating a flip card so we can write in the centre.

First side with my information at the director / licensee and then the back side with my assistant's details.

Inside with minimal information, facebook link/sign and then lines to write on.

www.norlandestates.com.au is my website to show colours and designs that I like.

Target Market(s)

Property Owners, Property Investors, Tenants, rental clients, Tradesman.

Industry/Entity Type

Business

Requirements
Must have
• Professional & symmetrical.

Am getting pro photos for myself & assistance, so a space for these once received.

```html
<!DOCTYPE html>
<html lang="en">
<head>
<meta charset="utf-8">
<title>Norland Estates – Fold Card</title>
<link rel="stylesheet" href="https://fonts.googleapis.com/css2?family=Oswald:wght@300;400;600;700&family=Open+Sans:wght@400;700&display=swap">
<style>
:root{
  --board:#d8d5cf;
  --ink:#1c1a17;
  --paper:#ffffff;
  --navy-deep:#0d1f2c;
  --navy:#17394a;
  --navy-light:#2d5a6d;
  --brand:#5b7d8f;
  --name-grey:#4f5a60;
  --text-blue:#2e4a66;
  --line:#5a6f8a;
  --ring:#d8111b;
}
*{box-sizing:border-box;margin:0;padding:0}
html,body{width:1200px;height:1000px;overflow:hidden}
body{background:var(--board);position:relative;font-family:"Open Sans",Arial,sans-serif;color:var(--ink)}
.abs{position:absolute}
.label{position:absolute;font-family:"Oswald",Arial,sans-serif;font-weight:600;color:var(--ink);white-space:nowrap}
.label--section{font-size:22px}
.label--title{font-size:30px;font-weight:600}
.label--view{font-size:28px}
.label--steps{font-size:26px;font-weight:700}

.panel{position:absolute;background:var(--paper);overflow:hidden}
.panel--dark{background:
  linear-gradient(160deg,transparent 30%,rgba(90,140,160,.25) 45%,transparent 60%),
  linear-gradient(180deg,var(--navy-deep) 0%,var(--navy) 45%,var(--navy-light) 70%,var(--navy-deep) 100%)}
.panel--fade{background:linear-gradient(180deg,var(--paper) 0%,var(--paper) 42%,#c8d0d4 48%,var(--navy) 56%,var(--navy-deep) 75%,var(--navy) 100%)}

.brand{position:absolute;font-family:"Oswald",Arial,sans-serif;font-weight:400;color:var(--brand);white-space:nowrap;text-align:center}

.person{position:absolute;left:24px;right:10px;white-space:nowrap}
.person__name{font-family:"Oswald",Arial,sans-serif;font-weight:700;color:var(--name-grey);font-size:36px;line-height:1}
.person__role,.person__line{font-family:"Open Sans",Arial,sans-serif;font-weight:700;color:#fff;font-size:9px;line-height:1;margin-top:9px}
.person--right .person__role,.person--right .person__line{padding-left:92px}

.write-line{position:absolute;left:30px;width:228px;border-top:1.5px dotted var(--line)}
.feather-slot{position:absolute;left:60px;top:28px;width:36px;height:70px;background:linear-gradient(150deg,#111,#444);border-radius:50% 10% 50% 10%}

.info{position:absolute;font-family:"Open Sans",Arial,sans-serif;font-weight:700;font-size:9px;color:var(--text-blue)}
.info dt{position:absolute;text-align:right;width:74px;white-space:nowrap}
.info dd{position:absolute;left:80px;white-space:nowrap}
.site{position:absolute;left:0;right:0;top:162px;text-align:center;font-family:"Oswald",Arial,sans-serif;font-weight:300;font-size:22px;color:#8fa0ad}

.step{position:absolute;font-family:"Open Sans",Arial,sans-serif;font-weight:700;font-size:12px;line-height:1.35;color:var(--ink)}
.step span{display:block;padding-left:36px}
</style>
</head>
<body>

<!-- Inside view -->
<div class="label label--section" style="left:147px;top:166px">Inside view of business card</div>
<div class="panel" style="left:30px;top:222px;width:48px;height:80px"></div>
<section class="panel" style="left:16px;top:300px;width:273px;height:280px" aria-label="Writing panel">
  <div class="feather-slot" role="img" aria-label="Feather quill illustration"></div>
  <div class="write-line" style="top:96px"></div>
  <div class="write-line" style="top:126px"></div>
  <div class="write-line" style="top:155px"></div>
  <div class="write-line" style="top:185px"></div>
  <div class="write-line" style="top:213px"></div>
</section>
<section class="panel" style="left:289px;top:208px;width:277px;height:372px;border-left:1px solid #e4e4e4" aria-label="Company details panel">
  <div class="brand" style="left:0;right:0;top:40px;font-size:34px">Norland Estates</div>
  <div class="site">WWW.NORLANDESTATES.COM.AU</div>
  <dl class="info" style="left:0;top:228px;width:277px">
    <dt style="top:0">Apply online:</dt><dd style="top:0">http://bit.ly/norland</dd>
    <dd style="top:20px">1300 NORLAND</dd>
    <dt style="top:37px">ACN:</dt><dd style="top:37px">000 111 222</dd>
    <dt style="top:75px">Postal Address:</dt><dd style="top:75px">Po Box 410, Bayview Q 4999</dd>
    <dt style="top:94px">Office Location:</dt><dd style="top:94px">Level 2/8 Harbour Parade, Bayview Q 4999</dd>
  </dl>
</section>

<!-- Covered view -->
<div class="label label--section" style="left:147px;top:584px">Covered view of business card</div>
<section class="panel panel--dark" style="left:17px;top:617px;width:277px;height:371px" aria-label="Assistant card">
  <div class="brand" style="left:0;right:0;top:130px;font-size:36px">Norland Estates</div>
  <div class="person" style="top:258px;left:10px">
    <div class="person__name">DANA MORRELL</div>
    <div class="person__role">Rental Manager</div>
    <div class="person__line">1300 555 010 &nbsp;| &nbsp;0400 555 272</div>
    <div class="person__line">dana@norlandestates.com.au</div>
  </div>
</section>
<div class="panel" style="left:503px;top:632px;width:50px;height:80px"></div>
<section class="panel panel--fade" style="left:294px;top:710px;width:272px;height:278px" aria-label="Director card, covered">
  <div class="person person--right" style="top:168px">
    <div class="person__name">CLARA WHITBY</div>
    <div class="person__role">Managing Director / Principal REA</div>
    <div class="person__line">1300 555 010 &nbsp;| &nbsp;0400 555 118</div>
    <div class="person__line">clara@norlandestates.com.au</div>
  </div>
</section>

<!-- Folded views -->
<div class="label label--title" style="left:660px;top:56px">View of Business Card when folded</div>
<div class="label label--view" style="left:703px;top:120px">Front view</div>
<div class="label label--view" style="left:981px;top:126px;font-size:24px;font-weight:700">Back view</div>

<section class="panel panel--fade" style="left:617px;top:180px;width:275px;height:370px" aria-label="Front of folded card">
  <div class="brand" style="left:0;right:0;top:44px;font-size:34px">Norland Estates</div>
  <div class="person person--right" style="top:258px">
    <div class="person__name">CLARA WHITBY</div>
    <div class="person__role">Managing Director / Principal REA</div>
    <div class="person__line">1300 555 010 &nbsp;| &nbsp;0400 555 118</div>
    <div class="person__line">clara@norlandestates.com.au</div>
  </div>
</section>
<section class="panel panel--dark" style="left:907px;top:180px;width:274px;height:370px" aria-label="Back of folded card">
  <div class="brand" style="left:0;right:0;top:130px;font-size:34px">Norland Estates</div>
  <div class="person" style="top:258px;left:10px">
    <div class="person__name">DANA MORRELL</div>
    <div class="person__role">Rental Manager</div>
    <div class="person__line">1300 555 010 &nbsp;| &nbsp;0400 555 272</div>
    <div class="person__line">dana@norlandestates.com.au</div>
  </div>
</section>

<!-- Folding steps -->
<div class="abs" style="left:870px;top:570px;width:330px;height:300px;background:radial-gradient(ellipse at center,#fff 45%,rgba(255,255,255,0) 72%)"></div>
<div class="brand" style="left:880px;top:660px;width:300px;font-size:46px">Norland Estates</div>
<svg class="abs" style="left:1090px;top:640px" width="40" height="200" viewBox="0 0 40 200" aria-hidden="true">
  <path d="M14 200 L14 40 L4 40 L20 0 L36 40 L26 40 L26 200 Z" fill="var(--ring)" opacity=".85"/>
</svg>
<div class="panel" style="left:1095px;top:850px;width:45px;height:70px"></div>
<div class="abs" style="left:912px;top:920px;width:243px;height:70px;background:linear-gradient(90deg,rgba(255,255,255,0),#fff 30%)"></div>
<svg class="abs" style="left:1055px;top:818px" width="104" height="146" viewBox="0 0 104 146" aria-hidden="true">
  <ellipse cx="52" cy="73" rx="48" ry="70" fill="none" stroke="var(--ring)" stroke-width="4"/>
</svg>

<div class="label label--steps" style="left:644px;top:644px">Steps to fold</div>
<p class="step" style="left:608px;top:722px">1st: make a curved slice inside the card
  <span>at the curved image part of the brand</span>
  <span>to make an opening.</span></p>
<p class="step" style="left:608px;top:852px">2nd: just simply insert the circled part of the card
  <span>to lock and close the card tightly.</span></p>

</body>
</html>
```